Marigold Compass One Pager

We are looking for an introductory one-pager to tell potential customers about our corporate training program. It is called Marigold Compass. Please see the added files below for detailed specs and requirements. Thank you!

Reason: Hi All, We are extending the project by a day, since we had slow submissions over the weekend. We are looking for a design that is pleasing/modern in look and feel - I think that we would prefer it to look artistic rather than corporate or industrial. I"knew to this, so please forgive me if my directions are vague, and please feel free to reach out for feedback.

Training

```html
<!DOCTYPE html>
<html lang="en">
<head>
<meta charset="utf-8">
<title>Marigold Compass One Pager</title>
<link rel="stylesheet" href="https://fonts.googleapis.com/css2?family=Bebas+Neue&family=Open+Sans:wght@400;700&display=swap">
<style>
  :root {
    --purple-top: #6b3f9c;
    --purple-bottom: #46176c;
    --green: #5ab43c;
    --silver: #c9c9d2;
    --lime: #d6e22a;
    --white: #ffffff;
    --photo-room: #b9a99a;
    --photo-cafe: #6e5a48;
    --divider: #5ab43c;
  }
  * { margin: 0; padding: 0; box-sizing: border-box; }
  html, body { width: 1200px; height: 927px; overflow: hidden; background: var(--white); }
  .page { position: relative; width: 1200px; height: 927px; overflow: hidden; font-family: "Open Sans", Arial, sans-serif; color: var(--white); }
  .photo { position: absolute; top: 0; height: 370px; }
  .photo--speaker { left: 0; width: 598px; background: linear-gradient(160deg, #d8cfc4 0%, var(--photo-room) 55%, #7c6c62 100%); }
  .photo--cafe { left: 605px; width: 595px; background: linear-gradient(200deg, #a88c6a 0%, var(--photo-cafe) 50%, #c9c0bc 100%); }
  .photo-divider { position: absolute; top: 0; left: 598px; width: 7px; height: 370px; background: var(--divider); }
  .base { position: absolute; inset: 0; width: 1200px; height: 927px; }
  .headline {
    position: absolute; left: 50px; top: 420px;
    font-family: "Bebas Neue", "Oswald", sans-serif;
    font-size: 52px; line-height: 47px; color: var(--lime); letter-spacing: 0.5px;
  }
  .list-title { font-weight: 700; font-size: 16.5px; line-height: 22px; }
  .bullets { list-style: none; font-size: 16.5px; }
  .bullets li::before { content: "• "; }
  .process { position: absolute; left: 50px; top: 608px; }
  .process .bullets { margin-top: 6px; line-height: 22.6px; }
  .value { position: absolute; left: 668px; top: 441px; }
  .value .bullets { line-height: 19.4px; }
</style>
</head>
<body>
<div class="page">
  <div class="photo photo--speaker" role="img" aria-label="Photo of a presenter with a microphone and clipboard addressing a seated audience in a banquet room"></div>
  <div class="photo photo--cafe" role="img" aria-label="Photo of a group of friends chatting over coffee at a cafe table"></div>
  <div class="photo-divider"></div>

  <svg class="base" viewBox="0 0 1200 927" aria-hidden="true">
    <defs>
      <linearGradient id="purpleFill" x1="0" y1="0" x2="0" y2="1">
        <stop offset="0" stop-color="var(--purple-top)"/>
        <stop offset="1" stop-color="var(--purple-bottom)"/>
      </linearGradient>
    </defs>
    <path d="M0,306 Q600,392 1200,304 L1200,927 L0,927 Z" fill="url(#purpleFill)"/>
    <path d="M0,306 Q600,392 1200,304" fill="none" stroke="var(--green)" stroke-width="9"/>
    <path d="M0,312 Q600,398 1200,310" fill="none" stroke="var(--silver)" stroke-width="2"/>
  </svg>

  <h1 class="headline">Something needs to change.<br>Do you have the<br>tools to get started?</h1>

  <section class="process">
    <h2 class="list-title">The Marigold Compass Process Is:</h2>
    <ul class="bullets">
      <li>Results-based, step by step process</li>
      <li>Inherently Energizing</li>
      <li>Community Oriented</li>
      <li>Relationship Enhancing</li>
      <li>Culture Building</li>
      <li>Silo-busting</li>
      <li>Simple But Challenging</li>
    </ul>
  </section>

  <section class="value">
    <h2 class="list-title">How Marigold Compass Initiatives Add Value:</h2>
    <ul class="bullets">
      <li>Super-charges your conversations</li>
      <li>Creates a shared vision</li>
      <li>Transforms relationships</li>
      <li>Empowers people to design change</li>
      <li>Creates optimal systems</li>
      <li>Delivers unique outcomes</li>
      <li>Supports conflict resolution</li>
      <li>Drives collaboration</li>
      <li>Enhances diversity</li>
      <li>Unites teams</li>
      <li>Uncovers root causes</li>
      <li>Increases innovation</li>
      <li>Ends dysfunctional patterns</li>
      <li>Generates trust</li>
      <li>Cultivates authentic leadership</li>
      <li>Increases engagement</li>
      <li>Promotes peer learning</li>
      <li>Builds resilience</li>
      <li>Activates networks</li>
      <li>Improves the caliber of interactions</li>
      <li>Supports stakeholder and client outcomes</li>
    </ul>
  </section>
</div>
</body>
</html>
```